3 x DIN A4 Flyer, Vorder- und Rückseite
Zielgruppe
Handwerksunternehmen
Aufgabenstellung
Wir benötigen 3 Werbeflyer die in Zeitschriften beigelegt werden. Jeweils DIN A4, Vorderseite beschreibt das Produkt, Rückseite kann zur Bestellung mittels Faxantwort benutzt werden. Profibilder und Text wird vollständig geliefert.

```html
<!DOCTYPE html>
<html lang="de">
<head>
<meta charset="utf-8">
<title>Kundenstopper – Flyer</title>
<link rel="stylesheet" href="https://fonts.googleapis.com/css2?family=Oswald:wght@600;700&family=PT+Sans:ital,wght@0,400;0,700;1,700&display=swap">
<style>
  :root {
    --orange: #f39231;
    --orange-deep: #ee7f1c;
    --ink: #4a4a4a;
    --ink-soft: #666;
    --paper: #ffffff;
    --price-yellow: #ffe21a;
    --photo-light: #d9dde1;
    --photo-dark: #9aa1a8;
  }
  * { box-sizing: border-box; margin: 0; padding: 0; }
  html, body { width: 933px; height: 1200px; overflow: hidden; background: var(--paper); }
  .flyer { position: relative; width: 933px; height: 1200px; background: var(--paper); font-family: "PT Sans", Arial, sans-serif; color: var(--ink); }

  .title-bar-left { position: absolute; left: 0; top: 73px; width: 46px; height: 76px; background: var(--orange); }
  .title-bar-right { position: absolute; left: 521px; top: 66px; width: 412px; height: 83px; background: var(--orange); }
  .headline { position: absolute; left: 62px; top: 58px; }
  .headline h1 { font-family: "Oswald", Impact, sans-serif; font-weight: 700; font-size: 60px; line-height: 66px; color: var(--orange); letter-spacing: 0.5px; }
  .headline p { font-family: "Oswald", Impact, sans-serif; font-weight: 600; font-size: 30px; line-height: 32px; color: var(--ink-soft); }

  .product-names { position: absolute; left: 70px; top: 224px; color: var(--orange); font-weight: 700; font-size: 22px; line-height: 29px; }
  .occasions { position: absolute; left: 70px; top: 360px; list-style: none; font-weight: 700; font-size: 18px; line-height: 23px; color: var(--ink-soft); }
  .formats { position: absolute; left: 70px; top: 515px; color: var(--orange); font-weight: 700; font-size: 18px; line-height: 22px; }

  .photo { position: absolute; background: linear-gradient(160deg, var(--photo-light), var(--photo-dark)); }
  .photo-main { left: 497px; top: 207px; width: 252px; height: 387px; }
  .photo-small { left: 62px; top: 646px; width: 145px; height: 290px; }
  .badge-new { position: absolute; left: 492px; top: 222px; width: 78px; height: 78px; border-radius: 50%; background: var(--orange); color: #fff; font-weight: 700; font-size: 18px; display: flex; align-items: center; justify-content: center; transform: rotate(-15deg); }

  .details { position: absolute; left: 352px; top: 680px; width: 540px; }
  .details h2 { color: var(--orange); font-weight: 700; font-size: 26px; line-height: 34px; margin-bottom: 6px; }
  .details ul { list-style: none; }
  .details li { position: relative; padding-left: 39px; font-size: 17px; line-height: 23px; color: var(--ink-soft); margin-bottom: 2px; }
  .details li::before { content: ""; position: absolute; left: 2px; top: 7px; width: 10px; height: 10px; background: var(--orange); }

  .company { position: absolute; left: 72px; top: 986px; width: 260px; }
  .company-name { font-weight: 700; font-size: 15px; line-height: 22px; color: var(--ink); }
  .company-address { margin-top: 16px; font-size: 15px; line-height: 21px; color: var(--ink-soft); }
  .company-web { margin-top: 24px; font-weight: 700; font-size: 17px; color: var(--ink); }

  .price-panel { position: absolute; left: 352px; top: 977px; width: 581px; height: 223px; background: var(--orange); }
  .price { position: absolute; left: 44px; top: 34px; font-family: "Oswald", Impact, sans-serif; font-weight: 700; font-size: 66px; line-height: 70px; color: var(--price-yellow); font-style: italic; text-shadow: 3px 3px 0 #7a3a00, -1px -1px 0 #7a3a00; }
  .price small { font-size: 26px; vertical-align: 28px; margin-left: 8px; }
  .price-note { position: absolute; left: 45px; top: 120px; width: 500px; font-size: 13px; line-height: 17px; color: #2d2d2d; }
</style>
</head>
<body>
<div class="flyer">
  <div class="title-bar-left"></div>
  <div class="title-bar-right"></div>
  <header class="headline">
    <h1>KUNDENSTOPPER</h1>
    <p>clever werben auf der Baustelle!</p>
  </header>

  <div class="product-names">
    Kundenstopper<br>Werbeständer<br>Gehwegaufsteller<br>Bockständer für Innen und Außen!
  </div>
  <ul class="occasions">
    <li>+ Messen</li>
    <li>+ Aktionstage</li>
    <li>+ Tag der offenen Tür</li>
    <li>+ Gewerbeveranstaltungen</li>
    <li>+ vor dem Betrieb</li>
  </ul>
  <div class="formats">Plakatformat!&nbsp; DIN A1 (60cm x 85cm)<br>Ständermaße! (121cm x 66cm)</div>

  <div class="photo photo-main" role="img" aria-label="Produktfoto: silberner Kundenstopper mit Klemmrahmen"></div>
  <div class="badge-new">NEU</div>
  <div class="photo photo-small" role="img" aria-label="Produktfoto: Kundenstopper mit Werbeplakat"></div>

  <section class="details">
    <h2>Produktdetails :</h2>
    <ul>
      <li>klappbares Standgestell</li>
      <li>2 aufmontierte Klemmrahmen mit 32 mm breitem Profil mit übergroßer Antireflex-Schutzfolie</li>
      <li>Ecken auf Gehrung geschnitten verzinkte Stahlblechrückwand (einseitig beschichtet)</li>
      <li>Antireflex-Schutzfolie, beidseitig nutzbar</li>
    </ul>
  </section>

  <address class="company" style="font-style:normal">
    <div class="company-name">KLTR Gesellschaft für<br>Handwerksbedarf mbH</div>
    <div class="company-address">Ahornweg 23<br>81234 München</div>
    <div class="company-web">www.kltr.de</div>
  </address>

  <div class="price-panel">
    <div class="price">39,-<small>netto</small></div>
    <p class="price-note">Alle angegebenen Preise verstehen sich in Euro zzgl. der gesetzlichen geltenden Mehrwertsteuer von derzeit 19%. Die Lieferung erfolgt ca.10 Tage nach Bestelleingang. Porto/Verpackung 12,90 Euro</p>
  </div>
</div>
</body>
</html>
```